Flyer Tally Your Ledger Free

Hi
Can you please design me a DL Flyer for: Tally Your Ledger Free
Info:
Starting a new Business ?
Want to save on bookkeeping fees for your existing business?

You can now save 1000's off bookkeeping fees by Doing it Yourself.

Using our Bookkeeper software you simply key in the information as you go.

We offer one on one training, backup and support.
We can assist you with BAS Preparation and Payrol Advice.

Add Modules as required:
Point of Sale Module
Jobs Management Module
Website Intergration Module

Fee set up assistance and training.

Lets get the ball rolling: 1300 642 815
www.tylfr.com.au
admin@tylfr.com.au (use the logo thing you made)

Target Market(s)

Small Business

Colors
ec1f27
f04a50
f59296
fcdcdc
ffffff

Requirements
Nice to have
• image/s related to bookkeeping

```html
<!DOCTYPE html>
<html lang="en">
<head>
<meta charset="utf-8">
<title>Tally Your Ledger Free – DL Flyer</title>
<link rel="stylesheet" href="https://fonts.googleapis.com/css2?family=Raleway:wght@400;500;600&family=Roboto+Condensed:wght@700&family=Arimo:wght@400;500&display=swap">
<style>
  :root{
    --red:#ec1f27;
    --red-soft:#f04a50;
    --red-pale:#f59296;
    --red-blush:#fcdcdc;
    --white:#ffffff;
    --ink:#2b2b2b;
    --grey:#4a4a4a;
    --dark:#333334;
    --stage:#ececec;
  }
  *{box-sizing:border-box;margin:0;padding:0}
  html,body{width:1200px;height:1200px;overflow:hidden;background:var(--stage)}
  .canvas{position:relative;width:1200px;height:1200px}
  .flyer{position:absolute;top:142px;width:445px;height:915px;background:var(--white);overflow:hidden;
    box-shadow:0 4px 14px rgba(0,0,0,.18);font-family:"Raleway",sans-serif;color:var(--ink)}
  .flyer--front{left:135px}
  .flyer--back{left:620px}
  .abs{position:absolute}
  .curves{position:absolute;left:0;top:0;width:445px;height:915px}

  /* front */
  .brand{left:36px;top:40px;display:flex;align-items:center;gap:12px}
  .brand__dot{width:30px;height:30px;border-radius:50%;background:var(--red)}
  .brand__name{font-size:30px;font-weight:600;color:var(--red);letter-spacing:-.3px}
  .photo-office{left:0;top:100px;width:445px;height:500px;
    background:linear-gradient(180deg,rgba(255,255,255,1) 0%,rgba(225,229,234,1) 14%,#c9d0d8 45%,#b9b3ae 75%,#a69d95 100%)}
  .badge{left:244px;top:420px;width:152px;height:152px;border-radius:50%;border:4px solid var(--white);
    background:radial-gradient(circle at 40% 35%,#5a5a5b,#2a2a2b 75%);box-shadow:0 3px 8px rgba(0,0,0,.35);
    color:var(--white);text-align:center;display:flex;flex-direction:column;justify-content:center}
  .badge__save{font-size:25px;font-weight:500;line-height:1}
  .badge__amount{font-family:"Roboto Condensed",sans-serif;font-weight:700;font-size:40px;line-height:1.02}
  .headline{left:40px;top:604px;font-family:"Roboto Condensed",sans-serif;font-weight:700;font-size:57px;line-height:.96;color:var(--red);letter-spacing:-.5px}
  .lede{left:40px;top:728px;font-size:20.5px;line-height:1.22;color:var(--grey)}
  .band{left:0;top:800px;width:445px;height:30px;font-family:"Arimo",sans-serif;font-weight:500;font-size:17.5px;
    color:var(--white);display:flex;align-items:center;justify-content:center;letter-spacing:.2px}
  .band--dark{background:var(--dark)}
  .band--red{background:var(--red)}
  .contact{left:39px;top:845px}
  .contact__label{font-size:14px;color:var(--ink)}
  .contact__phone{margin-top:5px;display:flex;align-items:center;gap:3px;font-family:"Arimo",sans-serif;font-size:26px;color:var(--ink)}
  .contact__web{left:255px;top:845px;font-size:14px;line-height:27px;color:var(--ink)}

  /* back */
  .photo-library{left:0;top:0;width:445px;height:410px;
    background:radial-gradient(ellipse at 55% 20%,#f2e6d6 0%,#c9a98a 30%,#7d5a45 62%,#4b352b 100%)}
  .intro{left:47px;top:414px;font-size:18.5px;font-weight:500;line-height:1.2;color:var(--red)}
  .body-copy{left:47px;top:466px;font-size:14.5px;line-height:1.22;color:var(--ink)}
  .support{left:0;top:516px;width:445px;height:90px;background:linear-gradient(90deg,#2f2f30,#555556 60%,#3a3a3b);
    color:var(--white);font-size:14.5px;line-height:1.22;padding:14px 40px 0 46px}
  .support p+p{margin-top:6px}
  .tab{left:90px;top:608px;width:265px;height:28px;background:var(--red);border-radius:0 0 5px 5px;
    font-family:"Roboto Condensed",sans-serif;font-weight:700;font-size:19.5px;color:var(--white);
    display:flex;align-items:center;justify-content:center}
  .module{top:658px;width:120px}
  .module__icon{width:60px;height:60px;display:block}
  .module__label{margin-top:6px;font-size:14.5px;line-height:1.25;color:var(--grey)}
</style>
</head>
<body>
<div class="canvas">

  <!-- Front of flyer -->
  <section class="flyer flyer--front">
    <div class="abs photo-office" role="img" aria-label="Photo of a smiling young woman working at a computer in an office with shelves of files"></div>
    <svg class="curves" viewBox="0 0 556 1144" aria-hidden="true">
      <path d="M0,643 Q110,660 210,712 Q360,610 556,566 L556,580 Q360,640 210,732 Q110,682 0,668Z" fill="var(--red)"/>
      <path d="M0,668 Q110,682 210,732 Q360,640 556,580 L556,1144 L0,1144Z" fill="var(--white)"/>
    </svg>
    <div class="abs brand"><span class="brand__dot"></span><span class="brand__name">Tally Your Ledger Free</span></div>
    <div class="abs badge">
      <span class="badge__save">save</span>
      <span class="badge__amount">1000'S<br>OFF</span>
    </div>
    <h1 class="abs headline">STARTING A<br>NEW BUSINESS?</h1>
    <p class="abs lede">Want to save on bookkeeping fees for<br>your existing business?</p>
    <div class="abs band band--dark">FEE SET UP ASSISTANCE AND TRAINING</div>
    <div class="abs contact">
      <div class="contact__label">Lets get the ball rolling:</div>
      <div class="contact__phone">
        <svg width="14" height="20" viewBox="0 0 14 20" aria-hidden="true"><path d="M5,1 L8,6 L5.5,8 Q5,11 7.5,14 L10,12.5 L13,17 L10,19.5 Q2,17 1.5,8 Q1.8,3 5,1Z" fill="var(--red)"/></svg>
        1300 642 815
      </div>
    </div>
    <div class="abs contact__web">www.tylfr.com.au<br>admin@tylfr.com.au</div>
  </section>

  <!-- Back of flyer -->
  <section class="flyer flyer--back">
    <div class="abs photo-library" role="img" aria-label="Photo of an open book with fanned pages in front of blurred library shelves"></div>
    <svg class="curves" viewBox="0 0 556 1144" aria-hidden="true">
      <path d="M0,405 Q110,415 213,478 Q360,375 556,338 L556,350 Q360,400 213,494 Q110,438 0,432Z" fill="var(--red)"/>
      <path d="M0,432 Q110,438 213,494 Q360,400 556,350 L556,1144 L0,1144Z" fill="var(--white)"/>
    </svg>
    <p class="abs intro">You can now save 1000's off bookkeeping<br>fees by Doing it Yourself.</p>
    <p class="abs body-copy">Using our Bookkeeper software you simply key in<br>the information as you go.</p>
    <div class="abs support">
      <p>We offer one on one training, backup and support.</p>
      <p>We can assist you with BAS Preparation and Payrol Advice.</p>
    </div>
    <div class="abs tab">ADD MODULES AS REQUIRED</div>

    <div class="abs module" style="left:48px">
      <svg class="module__icon" viewBox="0 0 60 60" aria-hidden="true">
        <path d="M30,3 L36,10 L45,8 L47,17 L56,20 L52,29 L57,37 L49,42 L49,51 L40,51 L35,58 L28,53 L20,57 L16,49 L7,47 L9,38 L3,31 L10,25 L8,16 L17,14 L21,6Z" fill="none" stroke="var(--red)" stroke-width="3" stroke-linejoin="round"/>
        <line x1="21" y1="40" x2="39" y2="20" stroke="var(--red)" stroke-width="3.5" stroke-linecap="round"/>
        <circle cx="22" cy="23" r="4.5" fill="none" stroke="var(--red)" stroke-width="3"/>
        <circle cx="38" cy="37" r="4.5" fill="none" stroke="var(--red)" stroke-width="3"/>
      </svg>
      <div class="module__label">Point of Sale<br>Module</div>
    </div>
    <div class="abs module" style="left:182px">
      <svg class="module__icon" viewBox="0 0 60 60" aria-hidden="true">
        <g fill="var(--red)">
          <rect x="26" y="1" width="8" height="10" rx="1"/><rect x="26" y="49" width="8" height="10" rx="1"/>
          <rect x="1" y="26" width="10" height="8" rx="1"/><rect x="49" y="26" width="10" height="8" rx="1"/>
          <rect x="26" y="1" width="8" height="10" rx="1" transform="rotate(45 30 30)"/><rect x="26" y="1" width="8" height="10" rx="1" transform="rotate(135 30 30)"/>
          <rect x="26" y="1" width="8" height="10" rx="1" transform="rotate(225 30 30)"/><rect x="26" y="1" width="8" height="10" rx="1" transform="rotate(315 30 30)"/>
          <circle cx="30" cy="30" r="21"/>
        </g>
        <circle cx="30" cy="30" r="14" fill="var(--white)"/>
        <circle cx="30" cy="26" r="5" fill="var(--red)"/>
        <path d="M20,40 Q30,28 40,40Z" fill="var(--red)"/>
      </svg>
      <div class="module__label">Jobs<br>Management<br>Module</div>
    </div>
    <div class="abs module" style="left:317px">
      <svg class="module__icon" viewBox="0 0 60 60" aria-hidden="true">
        <g fill="none" stroke="var(--red)" stroke-width="2.5">
          <path d="M34,50 L4,50 L4,4 L56,4 L56,36"/>
          <line x1="4" y1="12" x2="56" y2="12"/>
          <rect x="10" y="18" width="10" height="8"/>
          <line x1="25" y1="19" x2="48" y2="19"/><line x1="25" y1="25" x2="48" y2="25"/>
          <line x1="10" y1="32" x2="34" y2="32"/><line x1="10" y1="38" x2="30" y2="38"/>
          <circle cx="45" cy="46" r="6"/>
          <path d="M45,34 V38 M45,54 V58 M33,46 H37 M53,46 H57 M37,38 L40,41 M50,51 L53,54 M37,54 L40,51 M50,41 L53,38"/>
        </g>
      </svg>
      <div class="module__label">Website<br>Intergration<br>Module</div>
    </div>

    <div class="abs band band--red">FEE SET UP ASSISTANCE AND TRAINING</div>
    <div class="abs contact">
      <div class="contact__label">Lets get the ball rolling:</div>
      <div class="contact__phone">
        <svg width="14" height="20" viewBox="0 0 14 20" aria-hidden="true"><path d="M5,1 L8,6 L5.5,8 Q5,11 7.5,14 L10,12.5 L13,17 L10,19.5 Q2,17 1.5,8 Q1.8,3 5,1Z" fill="var(--red)"/></svg>
        1300 642 815
      </div>
    </div>
    <div class="abs contact__web">www.tylfr.com.au<br>admin@tylfr.com.au</div>
  </section>

</div>
</body>
</html>
```